Brackwell Immigration Law

We need a web design for our existing company www.brackwellcounsel.co.uk. We are an immigration consultancy. The final design should communicate professionalism, integrity and affordability.

Industry/Entity Type

It Company

Logo Text

Brackwell Counsel Partners

Number of Pages Required

5+ page

Font styles to use
Serif

Requirements
Must have
• I want to have the same silhouette logo but something different in positioning..
Nice to have
• Please have a look at these websites:
• https://www.travelpathguide.co.uk/visa_uk/
• http://www.oakdenadvisers.co.uk/
• http://www.myrtlegatelaw.org/index.php
• www.brackwellcounsel.co.uk

```html
<!DOCTYPE html>
<html lang="en">
<head>
<meta charset="utf-8">
<title>Brackwell Counsel Partners – Immigration Law</title>
<link rel="stylesheet" href="https://fonts.googleapis.com/css2?family=Open+Sans:wght@400;600;700&family=Lora:wght@400&display=swap">
<style>
  :root{
    --brand:#c71a4d;
    --brand-dark:#a8123e;
    --ink:#2e2e2e;
    --muted:#777777;
    --rule:#e4e4e4;
    --paper:#ffffff;
    --mist:#f3f3f3;
    --footer:#2a2a2a;
  }
  *{box-sizing:border-box;margin:0;padding:0}
  html,body{width:1200px;height:2440px;overflow:hidden}
  body{font-family:"Open Sans",Arial,sans-serif;color:var(--ink);background:var(--paper);position:relative}
  .wrap{width:1056px;margin:0 auto;position:relative}

  /* header */
  .site-header{height:100px;border-bottom:1px solid var(--rule)}
  .site-header .wrap{display:flex;justify-content:space-between;align-items:center;height:100px}
  .brand-name{font-family:"Lora",Georgia,serif;font-size:30px;color:var(--ink);line-height:1}
  .brand-tag{font-size:11px;letter-spacing:3px;color:var(--brand);margin-top:6px}
  .main-nav{display:flex;gap:6px;align-self:stretch}
  .main-nav a{display:flex;align-items:center;padding:0 18px;font-size:13px;font-weight:600;color:var(--ink);text-decoration:none;border-top:4px solid transparent}
  .main-nav a.active{border-top-color:var(--brand);color:var(--brand)}

  /* hero */
  .hero{height:580px;position:relative;overflow:hidden}
  .hero-photo{position:absolute;inset:0;background:linear-gradient(100deg,#d9d2cb 0%,#eef0f2 35%,#f6f7f8 60%,#dfe3e7 100%)}
  .hero-copy{position:absolute;right:72px;top:270px;text-align:right}
  .hero-lead{display:inline-block;background:rgba(40,40,40,.85);color:#fff;font-size:30px;font-weight:700;letter-spacing:1px;padding:8px 18px}
  .hero-main{display:block;background:rgba(255,255,255,.95);color:var(--brand);font-size:34px;font-weight:700;letter-spacing:1px;padding:8px 18px;margin-top:8px}
  .hero-arrows{position:absolute;right:72px;top:468px;display:flex;gap:10px}
  .hero-arrows span{width:36px;height:36px;border-radius:50%;background:#fff;display:flex;align-items:center;justify-content:center;box-shadow:0 1px 3px rgba(0,0,0,.2)}

  /* headings */
  .section-title{text-align:center;font-size:34px;font-weight:700;letter-spacing:2px;text-transform:uppercase}
  .btn{display:inline-block;background:var(--brand);color:#fff;font-size:12px;font-weight:700;letter-spacing:1px;text-transform:uppercase;padding:11px 24px;text-decoration:none}

  /* welcome */
  .welcome{height:288px;text-align:center;padding-top:62px}
  .welcome p{width:1000px;margin:22px auto 26px;font-size:14px;line-height:22px;color:var(--muted)}

  /* services */
  .services{height:552px;background:var(--brand);padding-top:52px}
  .services .section-title{color:#fff}
  .service-grid{display:grid;grid-template-columns:repeat(3,1fr);gap:24px 18px;margin-top:44px}
  .service-card{background:#fff;height:140px;display:flex;padding:8px}
  .service-photo{width:134px;flex:none;background:linear-gradient(135deg,#cfc7c0,#eceae7)}
  .service-body{padding:8px 4px 0 16px;display:flex;flex-direction:column}
  .service-body h3{font-size:14px;font-weight:700;text-transform:uppercase;letter-spacing:.5px}
  .service-body h3 em{font-style:normal;color:var(--brand)}
  .service-body p{font-size:12px;line-height:18px;color:var(--muted);margin-top:10px}
  .more{font-size:12px;font-weight:600;color:var(--ink);margin-top:auto;margin-bottom:6px;align-self:flex-end}

  /* team */
  .team{height:480px;padding-top:50px}
  .team-grid{display:grid;grid-template-columns:repeat(4,248px);gap:20px;margin-top:30px}
  .member{text-align:center}
  .member-photo{height:172px;background:linear-gradient(160deg,#bfd3e0,#e9eef2)}
  .member h3{color:var(--brand);font-size:14px;font-weight:700;text-transform:uppercase;margin-top:22px}
  .member p{font-size:12px;line-height:18px;color:var(--muted);margin:8px 12px 16px}
  .member .btn{padding:9px 20px;font-size:11px}

  /* news */
  .news{height:368px;background:var(--mist);padding-top:56px}
  .news-grid{display:grid;grid-template-columns:508px 520px;gap:28px;margin-top:40px}
  .news-card{background:#fff;height:178px;display:flex;padding:24px 22px}
  .news-date{width:84px;flex:none;text-align:center;color:var(--brand)}
  .news-date b{display:block;font-size:40px;line-height:1;font-weight:600}
  .news-date small{display:block;font-size:11px;font-weight:700;color:var(--ink);margin-top:4px}
  .news-body h3{color:var(--brand);font-size:15px;font-weight:700;text-transform:uppercase}
  .news-body p{font-size:12px;line-height:19px;color:var(--muted);margin:10px 0 12px}
  .news-body .more{display:block}

  /* footer */
  .site-footer{height:72px;background:var(--footer)}
  .site-footer .wrap{display:flex;justify-content:space-between;align-items:center;height:72px}
  .site-footer p{font-size:12px;color:#bbb}
  .social{display:flex;gap:8px}
  .social span{width:26px;height:26px;border-radius:50%;background:#e6e6e6}
</style>
</head>
<body>

<header class="site-header">
  <div class="wrap">
    <div class="brand">
      <div class="brand-name">Brackwell Counsel Partners</div>
      <div class="brand-tag">IMMIGRATION LAW</div>
    </div>
    <nav class="main-nav">
      <a class="active" href="#">HOME</a>
      <a href="#">ABOUT</a>
      <a href="#">JOIN</a>
      <a href="#">CONTACT</a>
      <a href="#">BLOG</a>
    </nav>
  </div>
</header>

<section class="hero">
  <div class="hero-photo" role="img" aria-label="Smiling consultant in a light office with colleagues seated behind"></div>
  <div class="hero-copy">
    <span class="hero-lead">WE ARE AN</span>
    <span class="hero-main">IMMIGRATION CONSULTANCY</span>
  </div>
  <div class="hero-arrows">
    <span><svg width="12" height="12" viewBox="0 0 12 12"><path d="M8 1 3 6l5 5" fill="none" stroke="#333" stroke-width="2"/></svg></span>
    <span><svg width="12" height="12" viewBox="0 0 12 12"><path d="M4 1l5 5-5 5" fill="none" stroke="#333" stroke-width="2"/></svg></span>
  </div>
</section>

<section class="welcome">
  <h2 class="section-title">Welcome to our site</h2>
  <p>Our advisers guide families, students and skilled workers through every stage of the UK immigration process. We explain each requirement clearly, prepare complete applications and keep you informed until a decision arrives. Fixed fees, honest advice and careful attention to detail mean fewer surprises and a stronger case from the very first consultation with our team.</p>
  <a class="btn" href="#">Learn more</a>
</section>

<section class="services">
  <div class="wrap">
    <h2 class="section-title">Our services</h2>
    <div class="service-grid">
      <article class="service-card">
        <div class="service-photo" role="img" aria-label="Young woman smiling"></div>
        <div class="service-body"><h3>Dependant <em>Visas</em></h3><p>Bring spouses and children to join you.</p><span class="more">More info &gt;</span></div>
      </article>
      <article class="service-card">
        <div class="service-photo" role="img" aria-label="Work permit paperwork"></div>
        <div class="service-body"><h3>Work permits</h3><p>Sponsorship and skilled worker routes for employers.</p><span class="more">More info &gt;</span></div>
      </article>
      <article class="service-card">
        <div class="service-photo" role="img" aria-label="Student studying at a desk"></div>
        <div class="service-body"><h3>Student <em>Visas</em></h3><p>Study visa applications for colleges and universities.</p><span class="more">More info &gt;</span></div>
      </article>
      <article class="service-card">
        <div class="service-photo" role="img" aria-label="Couple together"></div>
        <div class="service-body"><h3>Marriage <em>Visas</em></h3><p>Spouse and fiancé visas handled with care.</p><span class="more">More info &gt;</span></div>
      </article>
      <article class="service-card">
        <div class="service-photo" role="img" aria-label="Judge's gavel on a desk"></div>
        <div class="service-body"><h3>Civil <em>Visas</em></h3><p>Civil partner applications prepared start to finish.</p><span class="more">More info &gt;</span></div>
      </article>
      <article class="service-card">
        <div class="service-photo" role="img" aria-label="Business handshake"></div>
        <div class="service-body"><h3>Partnership <em>Visas</em></h3><p>Unmarried partner routes with full document checks.</p><span class="more">More info &gt;</span></div>
      </article>
    </div>
  </div>
</section>

<section class="team">
  <div class="wrap">
    <h2 class="section-title">Our team</h2>
    <div class="team-grid">
      <article class="member">
        <div class="member-photo" role="img" aria-label="Portrait of Anders Holloway"></div>
        <h3>Anders Holloway</h3>
        <p>Senior caseworker with ten years of family visa experience.</p>
        <a class="btn" href="#">Read more</a>
      </article>
      <article class="member">
        <div class="member-photo" role="img" aria-label="Portrait of Clara Wynne"></div>
        <h3>Clara Wynne</h3>
        <p>Advises students and graduates on study and work routes.</p>
        <a class="btn" href="#">Read more</a>
      </article>
      <article class="member">
        <div class="member-photo" role="img" aria-label="Portrait of Howard Pembry"></div>
        <h3>Howard Pembry</h3>
        <p>Leads business immigration and sponsor licence applications for employers.</p>
        <a class="btn" href="#">Read more</a>
      </article>
      <article class="member">
        <div class="member-photo" role="img" aria-label="Portrait of Vera Lindqvist"></div>
        <h3>Vera Lindqvist</h3>
        <p>Handles appeals, settlement and British citizenship cases for clients.</p>
        <a class="btn" href="#">Read more</a>
      </article>
    </div>
  </div>
</section>

<section class="news">
  <div class="wrap">
    <h2 class="section-title">Latest news</h2>
    <div class="news-grid">
      <article class="news-card">
        <div class="news-date"><b>02</b><small>JULY 2015</small></div>
        <div class="news-body"><h3>Finibus bonorum et malorum</h3><p>New guidance on family visa financial requirements comes into effect this month. Here is what applicants need to know.</p><span class="more">More info &gt;</span></div>
      </article>
      <article class="news-card">
        <div class="news-date"><b>06</b><small>JULY 2015</small></div>
        <div class="news-body"><h3>Finibus bonorum et malorum</h3><p>Processing times for student visas are shorter this summer. Apply early to secure your place before term begins.</p><span class="more">More info &gt;</span></div>
      </article>
    </div>
  </div>
</section>

<footer class="site-footer">
  <div class="wrap">
    <p>© 2015 by Brackwell Counsel Partners, All right reserved.</p>
    <div class="social"><span></span><span></span><span></span><span></span><span></span><span></span></div>
  </div>
</footer>

</body>
</html>
```